Komplette Präsentationsvorlage für Psychologen gewünscht
Zielgruppe
Ich bin Psychologe und trainiere in Seminaren Fach- und Führungskräften zu sozialen Kompetenzen.
Aufgabenstellung
Ich möchte eine PPT Vorlage / Folien-Master die folgende Kriterien erfüllt:
1. Passend zu meinem Corporate Design (Farben, Schriftarten, Logo) / Farbwerte #043D5D und #F15A29; Hintergrund überwiegend reinweiß und vereinzelt #D2D2D2
2. Folienmaster sollte folgendermaßen aufgebaut sein: oben rechts das Signet des Logos (Datei: Logo 546), unten rechts fortlaufende Seitenzahlen mit passendem Trenn-Symbol (*) in einer der beiden o.g. Farbwerte
3. Unten links das vollständige Logo in klein (Datei: Logo_2_346)
4. Vielfältige vorgestaltete Layout-Folien, die diverse Content-Darstellungen erlauben und in der Vorlage einprogrammiert sind (siehe unten)
Generell sollte sich das Gesamt-Design an der Vorlage eines Kunden orientieren, das für mich sehr passt. Ich lade zur Inspiration den betreffenden Folienmaster in den Dateien hoch.
Besonders wichtig ist mir Punkt 4 - in der benannten Inspirationsvorlage kann man diese reichhaltigen Layout-Folien gut einsehen durch Klick auf Einfügen > Neue Folien (das kleine Pfeil-Symbol). Vergleichbare Folien sollten bitte ebenfalls im Design gestaltet und genauso einprogrammiert sein, dass ich sie über Klick auf 'Neue Folien direkt auswählen kann. Der Schwerpunkt kann bei mir auf den Kategorien 'Titel und Inhalte', 'Text und Bild' liegen.
Weiterhin sollten auf den Folien ebenfalls verschiedene Grafiken / Piktogramme verfügbar sein, die einem gleichen Stil folgen (auch hier gefällt mir, der 'Comic/Skizzen' Stil meines Kunden sehr gut) - inhaltlich sollten die Grafiken vor allem soziale Situationen, Business-Themen, Verhandlungen, Speech, usw. betreffen. Gerne darf es auch eine Folie mit diversen Grafiken zur Auswahl als Sammlung geben.
(*) Ebenfalls in der Vorlage meines Kunden wird an diversen Stellen innerhalb der Präsentation ein abgerundeter roter 'Strich' verwendet, welcher auch als Trenn-Symbol für die Seitenzahl verwendet wird. Ich wünsche mir ein ähnlich durchgängig designt..

```html
<!DOCTYPE html>
<html lang="en">
<head>
<meta charset="utf-8">
<title>Slide Master – Henrik Valdenau</title>
<link href="https://fonts.googleapis.com/css2?family=Poppins:wght@400;600;700&family=Open+Sans:ital,wght@0,400;0,600;1,400&display=swap" rel="stylesheet">
<style>
:root{
  --navy:#043D5D;
  --orange:#F15A29;
  --grey:#D2D2D2;
  --grey-soft:#EEEEEE;
  --text:#3a3a3a;
  --page:#F4F4F4;
  --white:#FFFFFF;
  --illu-a:#DCE6F5;
  --illu-b:#4F79C6;
}
*{box-sizing:border-box;margin:0;padding:0}
html,body{width:1200px;height:2880px;overflow:hidden}
body{background:var(--page);font-family:"Open Sans",Arial,sans-serif;color:var(--text)}
.sheet{display:grid;grid-template-columns:540px 540px;column-gap:40px;row-gap:130px;padding:163px 40px}
.slide{position:relative;width:540px;height:304px;background:var(--white);overflow:hidden;box-shadow:0 2px 10px rgba(0,0,0,.06)}
.signet{position:absolute;top:20px;right:30px;width:24px;height:24px;border-radius:50%;background:var(--orange)}
.brand{position:absolute;left:24px;bottom:14px;display:flex;align-items:center;gap:5px;font-family:"Poppins",sans-serif;font-weight:600;font-size:7px;letter-spacing:.06em;color:var(--navy)}
.brand::before{content:"";width:10px;height:10px;border-radius:50%;background:var(--orange)}
.page-no{position:absolute;right:30px;bottom:12px;font-family:"Poppins",sans-serif;font-weight:600;font-size:10px;color:var(--navy);display:flex;align-items:center;gap:6px}
.page-no::before{content:"";width:2px;height:12px;border-radius:2px;background:var(--orange)}
.title{font-family:"Poppins",sans-serif;font-weight:700;font-size:17px;color:var(--navy);line-height:1.1}
.title span{color:var(--orange)}
.title.barred{padding-left:16px;position:relative}
.title.barred::before{content:"";position:absolute;left:0;top:0;width:3px;height:100%;border-radius:3px;background:var(--orange)}
.subtitle{font-family:"Poppins",sans-serif;font-size:10px;color:var(--navy);margin-top:2px}
.heading{position:absolute}
.body{position:absolute;font-size:7px;line-height:1.62}
.illu{position:absolute;border-radius:50% 45% 40% 50%;background:radial-gradient(circle at 50% 45%,var(--illu-b) 0%,#8EA9DD 35%,var(--illu-a) 70%,transparent 72%)}
.illu.block{border-radius:0;background:linear-gradient(135deg,#C9D7EE,#E8EEF8)}
.orange-sub{font-family:"Poppins",sans-serif;font-weight:600;font-size:9px;color:var(--orange)}
.cover-brand{position:absolute;left:38px;top:38px;display:flex;align-items:center;gap:8px}
.cover-brand .dot{width:22px;height:22px;border-radius:50%;background:var(--orange)}
.cover-brand .name{font-family:"Poppins",sans-serif;font-weight:600;font-size:12px;letter-spacing:.05em;color:var(--navy)}
.cover-brand .tag{font-family:"Poppins",sans-serif;font-weight:600;font-size:6.5px;letter-spacing:.1em;color:var(--navy)}
.cover-title{position:absolute;left:46px;top:128px;font-size:23px}
.cover-title.barred::before{width:4px}
.cover-url{position:absolute;left:66px;top:265px;font-family:"Poppins",sans-serif;font-weight:600;font-size:8px;color:var(--orange)}
.cover-disc{position:absolute;left:340px;top:0;width:290px;height:290px;border-radius:50%;background:var(--orange);transform:translateY(-10px)}
.quote-slide .band{position:absolute;inset:0 0 44px 0;background:var(--orange)}
.quote-slide .notch{position:absolute;left:26px;top:258px;width:0;height:0;border-left:8px solid transparent;border-right:8px solid transparent;border-top:8px solid var(--orange)}
.quote-slide .signet{background:var(--white)}
.quote-mark{position:absolute;left:40px;top:28px;font-family:"Poppins",sans-serif;font-weight:700;font-size:42px;line-height:1;color:var(--white)}
.quote-text{position:absolute;left:62px;top:78px;width:430px;font-family:"Poppins",sans-serif;font-style:italic;font-size:15.5px;line-height:1.52;color:var(--white)}
.quote-author{position:absolute;left:378px;top:222px;font-family:"Poppins",sans-serif;font-size:8.5px;color:var(--white);padding-left:10px;border-left:2px solid var(--white);line-height:1}
.aside-quote{position:absolute;left:270px;top:150px;width:270px;height:92px;background:var(--grey-soft);padding:12px 16px 0 22px;font-style:italic;font-size:8px;line-height:1.9;color:#777}
.aside-quote::before{content:"";position:absolute;left:8px;top:10px;width:2px;height:72px;border-radius:2px;background:var(--orange)}
.edge-band{position:absolute;left:0;top:0;width:12px;height:100%;background:var(--orange)}
.num{position:absolute;display:flex;gap:4px;font-size:7px;line-height:1.5}
.num b{font-family:"Poppins",sans-serif;font-weight:700;font-size:12px;color:var(--orange);line-height:1;flex:none}
.num.wide{width:118px}
.num.narrow{width:88px}
.big-head{position:absolute;left:38px;top:30px;font-family:"Poppins",sans-serif;font-weight:700;font-size:15px;line-height:1.22;color:var(--navy);padding-left:16px}
.big-head::before{content:"";position:absolute;left:0;top:2px;width:3px;height:22px;border-radius:3px;background:var(--orange)}
.big-head span{color:var(--orange)}
.grey-panel{position:absolute;left:0;top:0;width:168px;height:100%;background:var(--grey)}
.orange-box{position:absolute;left:52px;top:196px;width:170px;height:70px;background:var(--orange);padding:12px 16px;font-family:"Poppins",sans-serif;font-weight:700;font-size:13px;line-height:1.2;color:var(--white)}
.bullets{list-style:none;margin-top:6px}
.bullets li{position:relative;padding-left:10px;margin-bottom:4px}
.bullets li::before{content:"";position:absolute;left:0;top:5px;width:3px;height:3px;border-radius:50%;background:var(--navy)}
.col{position:absolute;top:92px;width:120px;font-size:7px;line-height:1.5}
.col .illu{position:relative;width:100px;height:60px;margin-bottom:14px}
.col .orange-sub{margin-bottom:6px;line-height:1.2}
</style>
</head>
<body>
<main class="sheet">

  <section class="slide">
    <div class="cover-brand"><div class="dot"></div><div><div class="name">HENRIK VALDENAU</div><div class="tag">TRAINING • BERATUNG • COACHING</div></div></div>
    <h1 class="title barred cover-title">Your Presentation<br><span>Title Goes Here</span></h1>
    <p class="body" style="left:66px;top:188px;width:210px">Lorem ipsum dolor sit amet, consectetur adipiscing elit, sed do eiusmod tempor incididunt ut labore et dolore magna aliqua. Ut enim ad minim veniam.</p>
    <p class="cover-url">www.henrik-valdenau.de</p>
    <div class="cover-disc"></div>
  </section>

  <section class="slide">
    <div class="signet"></div>
    <div class="illu" style="left:20px;top:65px;width:220px;height:190px" role="img" aria-label="Illustration of people building a word from large letter blocks beside a light bulb"></div>
    <div class="heading" style="left:258px;top:42px"><h2 class="title">Presentation <span>Title</span></h2>
      <div style="width:24px;height:2px;background:var(--orange);margin-top:12px;border-radius:2px"></div></div>
    <p class="body" style="left:258px;top:92px;width:250px">Lorem ipsum dolor sit amet, consectetur adipiscing elit, sed do eiusmod tempor incididunt ut labore et dolore magna aliqua. Ut enim ad minim veniam, quis nostrud exercitation ullamco laboris nisi ut aliquip ex ea commodo consequat. Duis aute irure dolor in reprehenderit in voluptate velit esse cillum dolore eu fugiat nulla pariatur. Excepteur sint occaecat cupidatat non proident, sunt in culpa qui officia deserunt mollit anim id est laborum. Lorem ipsum dolor sit amet, consectetur adipiscing elit, sed do eiusmod tempor incididunt ut labore et dolore magna aliqua. Ut enim ad minim veniam, quis nostrud exercitation ullamco laboris nisi ut aliquip Duis aute irure dolor in reprehenderit in voluptate velit esse cillum dolore eu fugiat nulla pariatur.</p>
    <div class="brand">HENRIK VALDENAU</div><div class="page-no">02</div>
  </section>

  <section class="slide">
    <div class="signet"></div>
    <h2 class="title barred heading" style="left:34px;top:42px">Presentation <span>Title</span></h2>
    <p class="body" style="left:34px;top:70px;width:470px">Lorem ipsum dolor sit amet, consectetur adipiscing elit, sed do eiusmod tempor incididunt ut labore et dolore magna aliqua. Ut enim ad minim veniam, quis nostrud exercitation ullamco laboris nisi ut aliquip ex ea commodo consequat. Lorem ipsum dolor sit amet, consectetur adipiscing elit, sed do eiusmod tempor incididunt ut labore et dolore magna aliqua. Ut enim ad minim veniam, quis nostrud exercitation ullamco laboris nisi ut aliquip ex ea commodo consequat.</p>
    <div class="illu" style="left:62px;top:145px;width:170px;height:118px" role="img" aria-label="Illustration of a woman with a megaphone on a large screen"></div>
    <div class="aside-quote">Lorem ipsum dolor sit amet, consectetur adipiscing elit, sed do eiusmod tempor incididunt ut labore et dolore magna aliqua. Ut enim ad minim veniam, quis nostrud exercitation.</div>
    <div class="brand">HENRIK VALDENAU</div><div class="page-no">03</div>
  </section>

  <section class="slide">
    <div class="signet"></div>
    <div class="heading" style="left:38px;top:32px"><h2 class="title barred">Presentation <span>Title</span><div class="subtitle">Your subtitle goes here</div></h2></div>
    <p class="body" style="left:38px;top:88px;width:225px">Lorem ipsum dolor sit amet, consectetur adipiscing elit, sed do eiusmod tempor incididunt ut labore et dolore magna aliqua. Ut enim ad minim veniam, quis nostrud exercitation ullamco laboris nisi ut aliquip ex ea commodo consequat. Duis aute irure dolor in reprehenderit in voluptate velit esse cillum dolore eu fugiat nulla pariatur. Excepteur sint occaecat cupidatat non proident, sunt in culpa qui officia deserunt mollit anim id est laborum. Lorem ipsum dolor sit amet, consectetur adipiscing elit, sed do eiusmod tempor incididunt ut labore et dolore magna aliqua. Ut enim ad minim veniam, quis nostrud exercitation ullamco laboris nisi ut aliquip Duis aute irure dolor in reprehenderit in voluptate velit esse cillum dolore eu fugiat nulla pariatur.</p>
    <div class="illu" style="left:290px;top:28px;width:215px;height:120px" role="img" aria-label="Illustration of a team meeting around a table with plants"></div>
    <p class="body" style="left:290px;top:172px;width:220px">Lorem ipsum dolor sit amet, consectetur adipiscing elit, sed do eiusmod tempor incididunt ut labore et dolore magna aliqua. Ut enim ad minim veniam, quis nostrud exercitation ullamco laboris nisi ut aliquip ex ea commodo consequat. Duis aute irure dolor in reprehenderit in voluptate velit esse cillum dolore eu fugiat nulla pariatur.</p>
    <div class="brand">HENRIK VALDENAU</div><div class="page-no">04</div>
  </section>

  <section class="slide">
    <div class="edge-band"></div>
    <div class="signet"></div>
    <div class="illu block" style="left:16px;top:55px;width:245px;height:205px;border-radius:40% 50% 10% 10%" role="img" aria-label="Illustration of a man at a desk in a video call with a woman"></div>
    <div class="heading" style="left:272px;top:32px"><h2 class="title barred">Presentation <span>Title</span><div class="subtitle">Your subtitle goes here</div></h2></div>
    <p class="body" style="left:272px;top:88px;width:225px">Lorem ipsum dolor sit amet, consectetur adipiscing elit, sed do eiusmod tempor incididunt ut labore et dolore magna aliqua. Ut enim ad minim veniam, quis nostrud exercitation ullamco laboris nisi ut aliquip ex ea commodo consequat. Duis aute irure dolor in reprehenderit in voluptate velit esse cillum dolore eu fugiat nulla pariatur. Excepteur sint occaecat cupidatat non proident, sunt in culpa qui officia deserunt mollit anim id est laborum. Lorem ipsum dolor sit amet, consectetur adipiscing elit, sed do eiusmod tempor incididunt ut labore et dolore magna aliqua. Ut enim ad minim veniam, quis nostrud exercitation ullamco laboris nisi ut aliquip Duis aute irure dolor in reprehenderit in voluptate velit esse cillum dolore eu fugiat nulla pariatur.</p>
    <div class="brand">HENRIK VALDENAU</div><div class="page-no">05</div>
  </section>

  <section class="slide quote-slide">
    <div class="band"></div><div class="notch"></div>
    <div class="signet"></div>
    <div class="quote-mark">“</div>
    <p class="quote-text">Lorem ipsum dolor sit amet, consectetur adipiscing elit, sed do eiusmod tempor incididunt ut labore et dolore magna aliqua. Ut enim ad minim veniam, quis nostrud exercitation ullamco laboris nisi ut aliquip ex ea commodo consequat.</p>
    <p class="quote-author">Max Mustermann</p>
    <div class="brand">HENRIK VALDENAU</div><div class="page-no">06</div>
  </section>

  <section class="slide">
    <div class="signet"></div>
    <div class="heading" style="left:38px;top:32px"><h2 class="title barred">Presentation <span>Title</span><div class="subtitle">Your subtitle goes here</div></h2></div>
    <div class="num wide" style="left:50px;top:96px"><b>1.</b><span>Lorem ipsum dolor sit amet, consectetur adipiscing elit.</span></div>
    <div class="num narrow" style="left:33px;top:164px"><b>2.</b><span>Lorem ipsum dolor sit amet, consecte-tur adipiscing elit.</span></div>
    <div class="num narrow" style="left:228px;top:80px"><b>3.</b><span>Lorem ipsum dolor sit amet, consecte-tur adipiscing elit.</span></div>
    <div class="num wide" style="left:404px;top:96px"><b>4.</b><span>Lorem ipsum dolor sit amet, consectetur adipiscing elit.</span></div>
    <div class="num narrow" style="left:430px;top:164px"><b>5.</b><span>Lorem ipsum dolor sit amet, consecte-tur adipiscing elit.</span></div>
    <div class="illu block" style="left:128px;top:134px;width:288px;height:132px;border-radius:8px;background:linear-gradient(90deg,#2E4A7A,#F3C23B 40%,#6FB3D6 70%,#F15A29)" role="img" aria-label="Illustration of a diverse group of business people walking together"></div>
    <div class="brand">HENRIK VALDENAU</div><div class="page-no">07</div>
  </section>

  <section class="slide">
    <div class="signet"></div>
    <h2 class="big-head">Lorem Ipsum<br>Dolor Sit Amet<br><span>Consectetur<br>Adipiscing Elit</span></h2>
    <p class="body" style="left:222px;top:34px;width:215px">Lorem ipsum dolor sit amet, consectetur adipiscing elit, sed do eiusmod tempor incididunt ut labore et dolore magna aliqua. Ut enim ad minim veniam, quis nostrud exercitation ullamco laboris nisi ut aliquip ex ea commodo consequat. Duis aute irure dolor in reprehenderit in voluptate velit esse cillum dolore eu fugiat nulla pariatur.</p>
    <div class="illu block" style="left:150px;top:130px;width:360px;height:142px;border-radius:12px;background:linear-gradient(90deg,#3E6DB8,#E9EEF7 45%,#3E6DB8)" role="img" aria-label="Illustration of a counselling session, two people seated in blue armchairs"></div>
    <div class="brand">HENRIK VALDENAU</div><div class="page-no">08</div>
  </section>

  <section class="slide">
    <div class="illu block" style="left:0;top:0;width:250px;height:304px;border-radius:0;background:linear-gradient(150deg,#8A2E4A,#E0387A 45%,#F15A29 80%,#F39A3A)" role="img" aria-label="Illustration of four diverse women shown in profile"></div>
    <div class="signet"></div>
    <h2 class="title barred heading" style="left:280px;top:36px">Presentation <span>Title</span></h2>
    <div class="body" style="left:280px;top:70px;width:225px">
      <p class="orange-sub">Your subtitle goes here</p>
      <p style="margin:3px 0 10px">Lorem ipsum dolor sit amet, consectetur adipiscing elit, sed do eiusmod tempor incididunt ut labore et dolore magna aliqua. Ut enim ad minim veniam.</p>
      <p class="orange-sub">Your subtitle goes here</p>
      <p style="margin:3px 0 10px">Lorem ipsum dolor sit amet, consectetur adipiscing elit, sed do eiusmod tempor incididunt ut labore et dolore magna aliqua. Ut enim ad minim veniam.</p>
      <p class="orange-sub">Your subtitle goes here</p>
      <p style="margin-top:3px">Lorem ipsum dolor sit amet, consectetur adipiscing elit, sed do eiusmod tempor incididunt ut labore et dolore magna aliqua. Ut enim ad minim veniam.</p>
    </div>
    <div class="page-no">09</div>
  </section>

  <section class="slide">
    <div class="grey-panel"></div>
    <div class="orange-box">Lorem Ipsum<br>Dolor Sit<br>Amet</div>
    <div class="signet"></div>
    <div class="heading" style="left:255px;top:32px"><h2 class="title barred">Presentation <span>Title</span><div class="subtitle">Your subtitle goes here</div></h2></div>
    <p class="body" style="left:255px;top:88px;width:225px">Lorem ipsum dolor sit amet, consectetur adipiscing elit, sed do eiusmod tempor incididunt ut labore et dolore magna aliqua. Ut enim ad minim veniam, quis nostrud exercitation ullamco laboris nisi ut aliquip ex ea commodo consequat. Duis aute irure dolor in reprehenderit in voluptate velit esse cillum dolore eu fugiat nulla pariatur. Excepteur sint occaecat cupidatat non proident, sunt in culpa qui officia deserunt mollit anim id est laborum. Lorem ipsum dolor sit amet, consectetur adipiscing elit, sed do eiusmod tempor incididunt ut labore et dolore magna aliqua. Ut enim ad minim veniam, quis nostrud exercitation ullamco laboris nisi ut aliquip Duis aute irure dolor in reprehenderit in voluptate velit esse cillum dolore eu fugiat nulla pariatur.</p>
    <div class="brand">HENRIK VALDENAU</div><div class="page-no">10</div>
  </section>

  <section class="slide">
    <div class="signet"></div>
    <div class="heading" style="left:46px;top:32px"><h2 class="title barred">Presentation <span>Title</span><div class="subtitle">Your subtitle goes here</div></h2></div>
    <div class="body" style="left:46px;top:92px;width:215px">
      <p>Lorem ipsum dolor sit amet, consectetur adipiscing elit, sed do eiusmod tempor incididunt ut labore et dolore magna aliqua. Ut enim ad minim veniam, quis nostrud exercitation ullamco laboris nisi ut aliquip.</p>
      <ul class="bullets">
        <li>Lorem ipsum dolor sit amet, consectetur adipiscing elit, sed do eiusmod tempor incididunt</li>
        <li>Lorem ipsum dolor sit amet, consectetur adipiscing elit, sed do eiusmod tempor incididunt</li>
        <li>Lorem ipsum dolor sit amet, consectetur adipiscing elit, sed do eiusmod tempor incididunt</li>
        <li>Lorem ipsum dolor sit amet, consectetur adipiscing elit, sed do eiusmod tempor incididunt</li>
      </ul>
    </div>
    <div class="illu" style="left:300px;top:95px;width:185px;height:150px" role="img" aria-label="Illustration of a team brainstorming under a large light bulb"></div>
    <div class="brand">HENRIK VALDENAU</div><div class="page-no">11</div>
  </section>

  <section class="slide">
    <div class="signet"></div>
    <div class="heading" style="left:38px;top:32px"><h2 class="title barred">Presentation <span>Title</span><div class="subtitle">Your subtitle goes here</div></h2></div>
    <div class="col" style="left:60px"><div class="illu" role="img" aria-label="Illustration of a presenter at a chart board"></div><p class="orange-sub">Your subtitle<br>goes here</p><p>Lorem ipsum dolor sit amet, consectetur adipiscing elit, sed do eiusmod tempor incididunt ut labore et dolore veniam.</p></div>
    <div class="col" style="left:210px"><div class="illu" role="img" aria-label="Illustration of a speaker on a large screen with listeners"></div><p class="orange-sub">Your subtitle<br>goes here</p><p>Lorem ipsum dolor sit amet, consectetur adipiscing elit, sed do eiusmod tempor incididunt ut labore et dolore veniam.</p></div>
    <div class="col" style="left:360px"><div class="illu" role="img" aria-label="Illustration of colleagues talking at a table"></div><p class="orange-sub">Your subtitle<br>goes here</p><p>Lorem ipsum dolor sit amet, consectetur adipiscing elit, sed do eiusmod tempor incididunt ut labore et dolore veniam.</p></div>
    <div class="brand">HENRIK VALDENAU</div><div class="page-no">12</div>
  </section>

</main>
</body>
</html>
```